Business Card design for Property Developer

We need a business card design for a Melbourne based Property Developer called "Kestrelmoor Holdings Pty Ltd".

We subdivide land and onsell to builders etc.

We already have a company logo, which is attached. Also I have attached the layout requirements from the printer. We would like a 2-sided design with one side displaying our logo by itself and the other with the required info, such as name, address, tel no., email, abn etc. The card will need to be used by 4 members of staff so name and contact details should be interchangable.
Updates

If possible, can you please write "name' "job position" "phone" "email" "address" on the card but leave them so I can add the details at a later time. Thank you. Also I plan on printing with UV spot printing as a background on the card. Keep this is mind when designing.

Thanks again.

Hello designers, please do not include pics of houses, house plansĀ or construction machinery etc as we really do not like the way it looks. Thank you.

Target Market(s)

Real Estate Agents, Land Owners, Local Council Departments, Govt Bodies, other Developers etc.

Industry/Entity Type

Business

Requirements
Must have
• 2-sided design with one side displaying our logo by itself and the other with the required info, such as name, address, tel no., email, abn etc.

```html
<!DOCTYPE html>
<html lang="en">
<head>
<meta charset="utf-8">
<title>Kestrelmoor Holdings – Business Card</title>
<link rel="stylesheet" href="https://fonts.googleapis.com/css2?family=Roboto+Condensed:ital,wght@0,700;0,800;1,700&family=PT+Sans:wght@400&display=swap">
<style>
  :root {
    --page-bg: #ffffff;
    --card-edge: #d9d9d9;
    --card-light: #ffffff;
    --card-mid: #f1f1f1;
    --card-shade: #e4e4e4;
    --brand-navy: #1f2a6b;
    --brand-blue: #3d6fc4;
    --text-dark: #1a1a1a;
  }
  * { margin: 0; padding: 0; box-sizing: border-box; }
  html, body {
    width: 1200px;
    height: 900px;
    overflow: hidden;
    background: var(--page-bg);
  }
  .canvas {
    position: relative;
    width: 1200px;
    height: 900px;
  }
  .card {
    position: absolute;
    left: 333px;
    width: 572px;
    height: 359px;
    border: 1px solid var(--card-edge);
    box-shadow: 0 1px 4px rgba(0,0,0,0.12);
    overflow: hidden;
  }
  .card--front { top: 57px; background: var(--card-mid); }
  .card--back {
    top: 483px;
    background: radial-gradient(ellipse at 50% 40%, var(--card-light) 0%, var(--card-light) 45%, var(--card-shade) 100%);
  }
  .spot-pattern {
    position: absolute;
    inset: 0;
    background: radial-gradient(ellipse at 50% 50%, #f6f6f6 0%, #ececec 70%, #e6e6e6 100%);
  }
  .brand {
    position: absolute;
    left: 0;
    right: 0;
    display: flex;
    flex-direction: column;
    align-items: center;
  }
  .brand__mark {
    border-radius: 50%;
    background: var(--brand-blue);
  }
  .brand__name {
    font-family: "Roboto Condensed", Arial, sans-serif;
    font-weight: 800;
    color: var(--brand-navy);
    text-transform: uppercase;
    letter-spacing: 0.5px;
    white-space: nowrap;
  }
  .card--front .brand { top: 88px; }
  .card--front .brand__mark { width: 118px; height: 118px; }
  .card--front .brand__name { margin-top: 20px; font-size: 33px; }

  .card--back .brand { top: 54px; }
  .card--back .brand__mark { width: 54px; height: 54px; }
  .card--back .brand__name { margin-top: 8px; font-size: 16px; }

  .person {
    position: absolute;
    left: 44px;
    top: 196px;
  }
  .person__name {
    font-family: "Roboto Condensed", Arial, sans-serif;
    font-weight: 800;
    font-size: 26px;
    line-height: 1;
    color: var(--brand-navy);
    letter-spacing: 0.2px;
  }
  .person__title {
    margin-top: 3px;
    font-family: "Roboto Condensed", Arial, sans-serif;
    font-weight: 700;
    font-style: italic;
    font-size: 15px;
    letter-spacing: 1px;
    color: var(--brand-navy);
  }
  .contact, .address {
    position: absolute;
    font-family: "PT Sans", Arial, sans-serif;
    font-size: 16.5px;
    line-height: 22px;
    color: var(--text-dark);
    list-style: none;
  }
  .contact { left: 44px; top: 255px; }
  .address { left: 366px; top: 233px; }
</style>
</head>
<body>
<main class="canvas">
  <section class="card card--front" aria-label="Card front">
    <div class="spot-pattern" role="img" aria-label="Faint UV spot pattern of repeating circular emblems across the card background"></div>
    <div class="brand">
      <span class="brand__mark" aria-hidden="true"></span>
      <span class="brand__name">Kestrelmoor Holdings</span>
    </div>
  </section>

  <section class="card card--back" aria-label="Card back">
    <div class="brand">
      <span class="brand__mark" aria-hidden="true"></span>
      <span class="brand__name">Kestrelmoor Holdings</span>
    </div>
    <div class="person">
      <p class="person__name">FIRSTNAME LASTNAME</p>
      <p class="person__title">Position Title</p>
    </div>
    <ul class="contact">
      <li>P 0411111111</li>
      <li>E name@kestrelmoorholdings.com</li>
    </ul>
    <ul class="address">
      <li>Address Line 1</li>
      <li>Address Line 2</li>
      <li>ABN: 11 111 111 111</li>
    </ul>
  </section>
</main>
</body>
</html>
```